WordPress Site That Reviews Footwear

We need a wordpress web design for an affiliate site called TreadNest. We review and do roundups on footwear products. The final design should be clean and mobile friendly. The site should be built with Gutenberg page builder. We like the design of https://dermalquill.com/.
Updates

Need extra days to review

Target Market(s)

USA

Industry/Entity Type

Footwear

Logo Text

TreadNest

Number of Pages Required

4 page

Font styles to use
Serif
Sans Serif

Requirements
Must have
• Wordpress site
Blog post
Page
Categories
Homepage

```html
<!DOCTYPE html>
<html lang="en">
<head>
<meta charset="utf-8">
<title>TreadNest – Footwear Reviews</title>
<link rel="stylesheet" href="https://fonts.googleapis.com/css2?family=DM+Serif+Display&family=Montserrat:wght@400;500;600;700&family=Lato:wght@400;700&display=swap">
<style>
:root{
  --ink:#1b1b1b;
  --text:#3d3d3d;
  --muted:#5a5a5a;
  --hero-green:#a3cf6a;
  --blush:#f4f0f1;
  --accent:#f9a602;
  --dark-panel:#2b2b2b;
  --footer:#000000;
  --white:#ffffff;
  --line:#dcdcdc;
}
*{margin:0;padding:0;box-sizing:border-box}
html,body{width:1200px;height:3486px;overflow:hidden}
body{position:relative;background:var(--white);color:var(--text);font-family:'Lato',sans-serif}
.abs{position:absolute}
.brand{font-family:'DM Serif Display',serif;color:var(--ink);font-weight:400}

/* header */
.site-header{position:absolute;left:0;top:0;width:1200px;height:89px;background:var(--white)}
.site-header .brand{left:134px;top:18px;font-size:38px;line-height:1}
.main-nav{position:absolute;top:38px;font-family:'Montserrat',sans-serif;font-size:14px;font-weight:500;color:var(--ink);letter-spacing:.2px}
.main-nav span{position:absolute;white-space:nowrap}

/* hero */
.hero{position:absolute;left:0;top:89px;width:1200px;height:582px;background:var(--hero-green)}
.hero-photo{position:absolute;left:0;top:0;width:600px;height:582px;background:radial-gradient(ellipse at 45% 55%,#d9dcd2 0%,#b9c79a 40%,var(--hero-green) 75%)}
.hero-title{position:absolute;left:644px;top:104px;width:480px;font-family:'DM Serif Display',serif;font-weight:400;font-size:43px;line-height:50px;letter-spacing:-.3px;color:var(--white)}
.hero-lead{position:absolute;left:646px;top:281px;width:420px;font-size:18px;line-height:26px;color:var(--white)}
.hero-btn{position:absolute;left:647px;top:366px;width:149px;height:51px;background:var(--white);color:var(--ink);font-family:'Montserrat',sans-serif;font-weight:500;font-size:17px;display:flex;align-items:center;justify-content:center}
.slide-arrow{position:absolute;top:270px;width:36px;height:43px;background:var(--white);display:flex;align-items:center;justify-content:center}
.slide-arrow.prev{left:0;border-radius:0 8px 8px 0}
.slide-arrow.next{right:0;border-radius:8px 0 0 8px}

/* section headings */
.section-title{position:absolute;font-family:'Montserrat',sans-serif;font-weight:600;color:var(--ink);font-size:20px;text-align:center;white-space:nowrap}
.rule{position:absolute;height:2px;background:#8a8a8a}

/* categories */
.categories{position:absolute;left:0;top:671px;width:1200px;height:387px;background:var(--blush)}
.cat{position:absolute;top:135px;width:169px;text-align:center}
.cat-photo{width:169px;height:169px;border-radius:50%}
.cat-name{margin-top:17px;font-size:16px;color:var(--ink)}
.cat-arrow{position:absolute;top:206px}

/* welcome */
.welcome{position:absolute;left:0;top:1058px;width:1200px;height:517px;background:var(--white)}
.welcome-photo{position:absolute;left:0;top:0;width:417px;height:517px;background:linear-gradient(160deg,#f3f3f3 0%,#d9d9d9 45%,#f5f5f5 100%)}
.welcome h2{position:absolute;left:567px;top:82px;font-family:'Montserrat',sans-serif;font-weight:600;font-size:23px;color:var(--ink)}
.welcome p{position:absolute;left:571px;top:158px;width:430px;font-size:16px;line-height:24px;color:var(--text)}
.btn-accent{position:absolute;background:var(--accent);color:var(--white);font-family:'Montserrat',sans-serif;font-weight:600;font-size:12px;display:flex;align-items:center;justify-content:center;letter-spacing:.3px}

/* product reviews */
.reviews{position:absolute;left:0;top:1575px;width:1200px;height:976px;background:var(--blush)}
.card{position:absolute;width:220px;height:358px;background:var(--white);border:1px solid var(--line);text-align:center}
.card-photo{position:absolute;left:30px;top:12px;width:160px;height:120px;border-radius:40%}
.stars{position:absolute;left:0;top:163px;width:100%;color:var(--accent);font-size:13px;letter-spacing:4px}
.card h3{position:absolute;left:12px;top:196px;width:196px;font-family:'Montserrat',sans-serif;font-weight:500;font-size:15px;line-height:19px;color:var(--ink)}
.card p{position:absolute;left:24px;top:240px;width:172px;font-size:11.5px;line-height:16px;color:var(--muted)}
.card .more{position:absolute;left:0;top:318px;width:100%;font-family:'Montserrat',sans-serif;font-weight:600;font-size:11.5px;color:var(--accent);text-decoration:underline}

/* features */
.features{position:absolute;left:0;top:2551px;width:1200px;height:575px;background:var(--white)}
.features-panel{position:absolute;left:0;top:0;width:656px;height:575px;background:var(--dark-panel)}
.feature-photo{position:absolute;left:557px;top:78px;width:512px;height:429px;background:linear-gradient(140deg,#4a3a33 0%,#6e7f8c 40%,#a77a4b 62%,#3c4a55 100%)}
.feature{position:absolute;left:137px;width:380px}
.feature svg{position:absolute;left:0;top:0}
.feature h4{position:absolute;left:90px;top:0;font-family:'Montserrat',sans-serif;font-weight:700;font-size:15px;color:var(--white);white-space:nowrap}
.feature p{position:absolute;left:90px;top:26px;width:245px;font-size:12px;line-height:16px;color:#d8d8d8}
.feature-rule{position:absolute;left:133px;width:367px;height:1px;background:#4a4a4a}

/* footer */
.site-footer{position:absolute;left:0;top:3126px;width:1200px;height:360px;background:var(--footer);color:var(--white)}
.site-footer .brand{position:absolute;left:135px;top:114px;color:var(--white);font-size:50px;line-height:1}
.foot-head{position:absolute;top:58px;font-family:'Montserrat',sans-serif;font-weight:700;font-size:13px;letter-spacing:.5px}
.foot-menu{position:absolute;left:461px;top:96px;font-family:'Montserrat',sans-serif;font-size:12px;line-height:20px;list-style:none}
.foot-item{position:absolute;font-size:12px;line-height:15px;white-space:nowrap}
.foot-item .dot{position:absolute;left:-34px;top:2px;width:24px;height:24px;border-radius:50%;background:var(--white);display:flex;align-items:center;justify-content:center}
.foot-rule{position:absolute;left:133px;top:274px;width:935px;height:1px;background:#2e2e2e}
.copyright{position:absolute;left:0;top:316px;width:1200px;text-align:center;font-size:10px;color:#cfcfcf}
</style>
</head>
<body>

<header class="site-header">
  <div class="brand abs">TreadNest</div>
  <nav class="main-nav">
    <span style="left:407px">HOME</span>
    <span style="left:478px">ABOUT US</span>
    <span style="left:578px">SERVICES</span>
    <span style="left:683px">REVIEWS</span>
    <span style="left:781px">CATEGORIES</span>
    <span style="left:910px">BLOG</span>
    <span style="left:981px">CONTACT US</span>
  </nav>
</header>

<section class="hero">
  <div class="hero-photo" role="img" aria-label="Close-up of feet wearing white strap sandals with rolled-up jeans"></div>
  <h1 class="hero-title">Lorem Ipsum is simply<br>dummy text of the<br>printing</h1>
  <p class="hero-lead">It is a long established fact that a reader will be distracted by the readable</p>
  <a class="hero-btn">READ MORE</a>
  <div class="slide-arrow prev"><svg width="10" height="14" viewBox="0 0 10 14"><path d="M7 2 2 7l5 5" fill="none" stroke="#222" stroke-width="1.6"/></svg></div>
  <div class="slide-arrow next"><svg width="10" height="14" viewBox="0 0 10 14"><path d="M3 2l5 5-5 5" fill="none" stroke="#222" stroke-width="1.6"/></svg></div>
</section>

<section class="categories">
  <h2 class="section-title" style="left:0;width:1180px;top:45px">CATEGORY BY REVIEWS</h2>
  <div class="rule" style="left:468px;top:74px;width:245px"></div>
  <svg class="cat-arrow" style="left:83px" width="16" height="26" viewBox="0 0 16 26"><path d="M13 3 3 13l10 10" fill="none" stroke="#333" stroke-width="2.4"/></svg>
  <svg class="cat-arrow" style="left:1100px" width="16" height="26" viewBox="0 0 16 26"><path d="M3 3l10 10-10 10" fill="none" stroke="#333" stroke-width="2.4"/></svg>
  <div class="cat" style="left:134px"><div class="cat-photo" role="img" aria-label="Dark slide sandals on grass" style="background:radial-gradient(circle,#4b5a6e,#2f3d2a)"></div><div class="cat-name">Lorem ipsum</div></div>
  <div class="cat" style="left:324px"><div class="cat-photo" role="img" aria-label="Black patent leather shoe" style="background:radial-gradient(circle at 40% 40%,#d5d5d5,#1d1d1d 70%)"></div><div class="cat-name">Lorem ipsum</div></div>
  <div class="cat" style="left:513px"><div class="cat-photo" role="img" aria-label="Brown lace-up boots on pavement" style="background:radial-gradient(circle,#6b3a26,#8d9196 70%)"></div><div class="cat-name">Lorem ipsum</div></div>
  <div class="cat" style="left:700px"><div class="cat-photo" role="img" aria-label="Pair of beige heels on wooden floor" style="background:radial-gradient(circle,#b89b76,#4a2a16 75%)"></div><div class="cat-name">Lorem ipsum</div></div>
  <div class="cat" style="left:897px"><div class="cat-photo" role="img" aria-label="Feet in peach sandals on turquoise background" style="background:radial-gradient(circle,#f2b79a,#7fe2e0 60%)"></div><div class="cat-name">Lorem ipsum</div></div>
</section>

<section class="welcome">
  <div class="welcome-photo" role="img" aria-label="Legs in star-patterned tights wearing black ankle boots"></div>
  <h2>WELCOME TO TREADNEST</h2>
  <div class="rule" style="left:571px;top:125px;width:306px"></div>
  <p>Lorem ipsum dolor sit amet, consectetur adipiscing elit, sed do eiusmod tempor incididunt ut labore et dolore magna aliqua. Ut enim ad minim veniam, quis nostrud exercitation ullamco laboris nisi ut aliquip ex ea commodo consequat. Duis aute irure dolor in reprehenderit in voluptate velit esse cillum dolore eu fugiat nulla pariatur. Excepteur sint occaecat cupidatat non proident, sunt in culpa qui officia deserunt mollit .</p>
  <a class="btn-accent" style="left:571px;top:388px;width:110px;height:38px">READ MORE</a>
</section>

<section class="reviews">
  <h2 class="section-title" style="left:0;width:1200px;top:50px">PRODUCT REVIEWS</h2>

  <article class="card" style="left:133px;top:126px"><div class="card-photo" role="img" aria-label="Red high heels" style="background:radial-gradient(circle,#d61e2a,#fff 70%)"></div><div class="stars">★★★★★</div><h3>Lorem ipsum dolor sit amet consectetur a</h3><p>Lorem ipsum dolor sit amet, consectetur adipiscing elit, se d do eiusmod tempor incid idunt ut labore et.</p><a class="more">READ MORE</a></article>
  <article class="card" style="left:371px;top:126px"><div class="card-photo" role="img" aria-label="Black canvas sneakers" style="background:radial-gradient(circle,#222,#fff 70%)"></div><div class="stars">★★★★★</div><h3>Lorem ipsum dolor sit amet consectetur a</h3><p>Lorem ipsum dolor sit amet, consectetur adipiscing elit, se d do eiusmod tempor incid idunt ut labore et.</p><a class="more">READ MORE</a></article>
  <article class="card" style="left:609px;top:126px"><div class="card-photo" role="img" aria-label="Olive military boots" style="background:radial-gradient(circle,#6b6a48,#fff 70%)"></div><div class="stars">★★★★★</div><h3>Lorem ipsum dolor sit amet consectetur a</h3><p>Lorem ipsum dolor sit amet, consectetur adipiscing elit, se d do eiusmod tempor incid idunt ut labore et.</p><a class="more">READ MORE</a></article>
  <article class="card" style="left:846px;top:126px"><div class="card-photo" role="img" aria-label="Light blue running shoes" style="background:radial-gradient(circle,#6cb6e0,#fff 70%)"></div><div class="stars">★★★★★</div><h3>Lorem ipsum dolor sit amet consectetur a</h3><p>Lorem ipsum dolor sit amet, consectetur adipiscing elit, se d do eiusmod tempor incid idunt ut labore et.</p><a class="more">READ MORE</a></article>

  <article class="card" style="left:133px;top:502px"><div class="card-photo" role="img" aria-label="Nude pointed heels" style="background:radial-gradient(circle,#f2c2aa,#fff 70%)"></div><div class="stars">★★★★★</div><h3>Lorem ipsum dolor sit amet consectetur a</h3><p>Lorem ipsum dolor sit amet, consectetur adipiscing elit, se d do eiusmod tempor incid idunt ut labore et.</p><a class="more">READ MORE</a></article>
  <article class="card" style="left:371px;top:502px"><div class="card-photo" role="img" aria-label="Grey slide slippers" style="background:radial-gradient(circle,#b8bcc0,#fff 70%)"></div><div class="stars">★★★★★</div><h3>Lorem ipsum dolor sit amet consectetur a</h3><p>Lorem ipsum dolor sit amet, consectetur adipiscing elit, se d do eiusmod tempor incid idunt ut labore et.</p><a class="more">READ MORE</a></article>
  <article class="card" style="left:609px;top:502px"><div class="card-photo" role="img" aria-label="Navy sport sandals" style="background:radial-gradient(circle,#34456e,#fff 70%)"></div><div class="stars">★★★★★</div><h3>Lorem ipsum dolor sit amet consectetur a</h3><p>Lorem ipsum dolor sit amet, consectetur adipiscing elit, se d do eiusmod tempor incid idunt ut labore et.</p><a class="more">READ MORE</a></article>
  <article class="card" style="left:846px;top:502px"><div class="card-photo" role="img" aria-label="Brown heeled ankle boots" style="background:radial-gradient(circle,#8a5a3e,#fff 70%)"></div><div class="stars">★★★★★</div><h3>Lorem ipsum dolor sit amet consectetur a</h3><p>Lorem ipsum dolor sit amet, consectetur adipiscing elit, se d do eiusmod tempor incid idunt ut labore et.</p><a class="more">READ MORE</a></article>

  <a class="btn-accent" style="left:553px;top:897px;width:95px;height:38px">VIEW ALL</a>
</section>

<section class="features">
  <div class="features-panel"></div>
  <div class="feature-photo" role="img" aria-label="Tan lace-up boots and jeans stepping outdoors"></div>

  <div class="feature" style="top:79px">
    <svg width="66" height="60" viewBox="0 0 66 60" fill="none" stroke="#f9a602" stroke-width="3.5" stroke-linejoin="round"><rect x="3" y="8" width="52" height="36" rx="2"/><path d="M22 44l-4 10h24l-4-10M12 54h36"/><circle cx="40" cy="18" r="10"/><path d="M47 25l10 10"/><path d="M10 36l10-10 8 6 8-8"/></svg>
    <h4>LOREM IPSUM DOLOR SIT</h4>
    <p>Lorem ipsum dolor sit amet, consectetur adipiscing elit, se d do eiusmod tempor incid idunt ut labore et.content of a page when looking at its layout.</p>
  </div>
  <div class="feature-rule" style="top:197px"></div>
  <div class="feature" style="top:232px">
    <svg width="66" height="66" viewBox="0 0 66 66" fill="none" stroke="#f9a602" stroke-width="3.5" stroke-linejoin="round"><path d="M31 4 8 12v20c0 15 11 24 23 30 12-6 23-15 23-30V12z"/><path d="M20 33l8 8 15-16"/></svg>
    <h4>LOREM IPSUM DOLOR SIT</h4>
    <p>Lorem ipsum dolor sit amet, consectetur adipiscing elit, se d do eiusmod tempor incid idunt ut labore et.content of a page when looking at its layout.</p>
  </div>
  <div class="feature-rule" style="top:358px"></div>
  <div class="feature" style="top:405px">
    <svg width="66" height="66" viewBox="0 0 66 66" fill="none" stroke="#f9a602" stroke-width="3.5" stroke-linejoin="round"><path d="M44 30V8a3 3 0 0 0-3-3H9a3 3 0 0 0-3 3v48a3 3 0 0 0 3 3h20"/><path d="M14 16h22M14 25h22M14 34h14"/><path d="M50 30l8 8-18 18-10 2 2-10z"/></svg>
    <h4>LOREM IPSUM DOLOR SIT</h4>
    <p>Lorem ipsum dolor sit amet, consectetur adipiscing elit, se d do eiusmod tempor incid idunt ut labore et.content of a page when looking at its layout.</p>
  </div>
</section>

<footer class="site-footer">
  <div class="brand">TreadNest</div>

  <div class="foot-head" style="left:461px">MENU</div>
  <ul class="foot-menu">
    <li>HOME</li><li>ABOUT US</li><li>SERVICES</li><li>REVIEWS</li><li>CATEGORIES</li><li>BLOG</li><li>CONTACT US</li>
  </ul>

  <div class="foot-head" style="left:662px">CONTACT US</div>
  <div class="foot-item" style="left:694px;top:96px"><span class="dot"><svg width="10" height="13" viewBox="0 0 10 13"><path d="M5 0a5 5 0 0 0-5 5c0 3.5 5 8 5 8s5-4.5 5-8a5 5 0 0 0-5-5z" fill="#000"/><circle cx="5" cy="5" r="1.8" fill="#fff"/></svg></span>2750 Maple Ridge Road<br>Lindale, CA 94021</div>
  <div class="foot-item" style="left:694px;top:147px"><span class="dot"><svg width="12" height="12" viewBox="0 0 12 12"><path d="M2.5 1 4.5 3.5 3.4 5a7 7 0 0 0 3.6 3.6L8.5 7.5 11 9.5 9.8 11C5 11 1 7 1 2.2z" fill="#000"/></svg></span>Call Us<br>555.010.4827</div>
  <div class="foot-item" style="left:694px;top:198px"><span class="dot"><svg width="12" height="9" viewBox="0 0 12 9"><rect width="12" height="9" rx="1" fill="#000"/><path d="M1 1l5 4 5-4" stroke="#fff" fill="none"/></svg></span>E mail Us<br>info@treadnest.com</div>

  <div class="foot-head" style="left:962px">FOLLOW US</div>
  <div class="foot-item" style="left:997px;top:96px"><span class="dot"></span>Like us on<br>FOLKSPACE</div>
  <div class="foot-item" style="left:997px;top:145px"><span class="dot"></span>Follow us on<br>CHIRPLINE</div>
  <div class="foot-item" style="left:997px;top:196px"><span class="dot"></span>Follow us on<br>LINKWORK</div>

  <div class="foot-rule"></div>
  <div class="copyright">Copyright © 2021 All Rights Reserved</div>
</footer>

</body>
</html>
```